BRACKENRIDGE BUILDERS B-Card

I currently have a b-card design but will be removing the image (tree) from the logo and have text only.
I want the card to be classy and strong within the building and construction industry.
I will be using Spot UV on the cards as per the attached examples. I will also send through some sketched ideas that I have in mind.
The color blue is similar to the image (No. 6) attached images

Target Market(s)

middle to maturre aged.
Home Owners / Renovators and Builders

Industry/Entity Type

Construction

Contact Information for Business Card

BRACKENRIDGE BUILDERS
Name: Dermot Quaile
Title: Project Manager
Mobile: 0412 537 804
Office: (08) 9173 5842
Address: 17C Pellworth Avenue, Thornvale WA 6071
Email: info@brackenridgebuild.com.au
PO Box: 3817 Thornvale WA 6915

Colors
0592cd
33a6d7
85cae6
1b1b1b

Requirements
Must have
• 1. It must have spot UV on the front of card, maybe back of card too
• 2. I really like the blue on image 6. (or at least a really cool electric blue against the charcoal grey background)
• 3. The font must be slimline and modern. Easy to read
• 4. There must be no black used on the card... Only greys and dark charcoal greys
• 5. Use only the text from the logo "Brackenridge Builders" Not the image of the tree. I am wanting the b-cards to be more masculine.
Nice to have
• 1. I like the design concept on image 6. but happy to see what else you can do with the Spot UV
• 2. Unless you have a really cool idea of the image of the tree (from previous logo) Spot UV somewhere in the design concept thats original and different then I am keen to see what you come up with
• 3. Try changing the color of the logo eg. full white or Blue and white
• 4. Another option is to have the Brackenridge Logo on the front of card with the spot UV in the background of text which we specialise in eg, Roofing, Ceiling, Insulation, Gutter Guards, Electrical, Insurance etc and we can add or reduce items as required. Similar to image 12.
Should not have
• Do not include the image of the tree from previous logo. unless you have a really cool idea of Spot UV somewhere in the design concept thats original and different.

```html
<!DOCTYPE html>
<html lang="en">
<head>
<meta charset="utf-8">
<title>Brackenridge Builders – Business Card</title>
<link rel="stylesheet" href="https://fonts.googleapis.com/css2?family=Open+Sans:wght@300;400;600;700&display=swap">
<style>
  :root {
    --blue: #33a6d7;
    --blue-deep: #0592cd;
    --blue-soft: #85cae6;
    --charcoal: #1b1b1b;
    --charcoal-mid: #262626;
    --ink: #2a2a2a;
    --paper: #ffffff;
    --backdrop: #e9e7e3;
  }
  * { margin: 0; padding: 0; box-sizing: border-box; }
  html, body {
    width: 1200px; height: 900px; overflow: hidden;
    background: var(--backdrop);
    font-family: "Open Sans", Arial, sans-serif;
  }
  .stage { position: relative; width: 1200px; height: 900px; }
  .card {
    position: absolute; left: 250px; width: 700px; height: 400px;
    overflow: hidden; box-shadow: 0 6px 18px rgba(0,0,0,0.18);
  }
  /* Back of card */
  .card-back { top: 35px; background: var(--charcoal); }
  .card-back .texture {
    position: absolute; inset: 0;
    background: radial-gradient(ellipse at 45% 55%, #2e2e2e 0%, var(--charcoal-mid) 40%, var(--charcoal) 75%);
  }
  .card-back .wordmark {
    position: absolute; left: 0; right: 0; top: 150px; text-align: center;
  }
  /* Front of card */
  .card-front { top: 465px; background: var(--paper); }
  .corner-mark { position: absolute; left: 0; top: 0; }
  .person { position: absolute; left: 78px; top: 22px; }
  .person .name { color: var(--blue); font-weight: 700; font-size: 19px; line-height: 1.1; }
  .person .title { color: var(--ink); font-size: 13px; }
  .contact {
    position: absolute; left: 38px; top: 168px;
    color: var(--ink); font-size: 14.5px; line-height: 1.45;
  }
  .contact .phone { display: flex; align-items: center; gap: 8px; padding-left: 14px; }
  .contact .phone svg { width: 12px; height: 12px; }
  .contact .address { margin-top: 8px; }
  .contact strong { font-weight: 700; }
  .card-front .wordmark { position: absolute; left: 300px; top: 140px; }
  .wordmark .name-line {
    display: block; color: var(--blue); font-weight: 700;
    font-size: 44px; letter-spacing: 0.5px; line-height: 1;
  }
  .wordmark .sub-line {
    display: block; color: var(--blue); font-weight: 300;
    font-size: 20px; letter-spacing: 14px; margin-top: 6px; line-height: 1;
  }
  .card-front .wordmark .name-line { font-size: 40px; }
  .card-front .wordmark .sub-line { font-size: 18px; letter-spacing: 12px; color: var(--ink); }
  .base-bands { position: absolute; left: 0; bottom: 0; }
</style>
</head>
<body>
<main class="stage">

  <section class="card card-back" aria-label="Business card back">
    <div class="texture" role="img" aria-label="Faint tonal leaf-and-branch background in spot UV"></div>
    <div class="wordmark">
      <span class="name-line">BRACKENRIDGE</span>
      <span class="sub-line">BUILDERS</span>
    </div>
  </section>

  <section class="card card-front" aria-label="Business card front">
    <svg class="corner-mark" width="70" height="56" viewBox="0 0 70 56" aria-hidden="true">
      <polygon points="0,0 40,0 0,40" fill="#33a6d7"/>
      <polygon points="44,0 66,0 48,52 8,52" fill="#1b1b1b"/>
    </svg>

    <div class="person">
      <div class="name">Dermot Quaile</div>
      <div class="title">Project Manager</div>
    </div>

    <div class="contact">
      <div class="phone">
        <svg viewBox="0 0 12 12" aria-hidden="true"><rect x="3" y="0.5" width="6" height="11" rx="1.2" fill="none" stroke="#33a6d7" stroke-width="1.2"/><circle cx="6" cy="9.5" r="0.7" fill="#33a6d7"/></svg>
        <span>0412 537 804</span>
      </div>
      <div class="phone">
        <svg viewBox="0 0 12 12" aria-hidden="true"><path d="M2.5 1 L4.5 1 L5.2 3.5 L4 4.6 C4.7 6.2 5.8 7.3 7.4 8 L8.5 6.8 L11 7.5 L11 9.5 C11 10.3 10.3 11 9.5 11 C5.4 10.7 1.3 6.6 1 2.5 C1 1.7 1.7 1 2.5 1 Z" fill="#33a6d7"/></svg>
        <span>(08) 9173 5842</span>
      </div>
      <div class="address">
        17C Pellworth Avenue,<br>
        Thornvale WA 6071<br>
        <strong>PO Box:</strong> 3817 Thornvale WA 6915
      </div>
    </div>

    <div class="wordmark">
      <span class="name-line">BRACKENRIDGE</span>
      <span class="sub-line">BUILDERS</span>
    </div>

    <svg class="base-bands" width="700" height="100" viewBox="0 0 700 100" aria-hidden="true">
      <polygon points="0,22 0,40 240,62 258,48" fill="#33a6d7"/>
      <polygon points="268,50 700,64 700,100 232,100" fill="#1b1b1b"/>
    </svg>
  </section>

</main>
</body>
</html>
```